flyer/brochure design to deliver to homes (letter box delivery)

Hi I would like something designed to represent my business Hair & Make up, I have a home based salon but offer mobile services for weddings. I really like beachy colours elegant and not to busy. but open to all different designs.

I will be getting these printed up through Tolvane Press the product specs are:

Document Trim Size
Horizontal
216 x 139 mm
2556 x 1642 pixels
Vertical
139 x 216 mm
1642 x 2556 pixels

Full Bleed Size
Horizontal
219 x 142 mm
2592 x 1677 pixels
Vertical
142 x 219 mm
1677 x 2592 pixels
Finished artwork should use the full bleed dimensions for best results.

I will also upload a recent business card that i have but dont have to stick to similar design

Reason: To give u more time

Industry/Entity Type

Salon

Requirements
Must have
• my logo (you can change the colour of my logo if you like)

would like it to have somewhere:
"look good feel great without paying silly prices"

must also have:

private home salon based in Corallin bay, mobile service provided for weddings only

Im thinking I would like the price list on the back but open to what ever you submit

price list:
Ladies Cut $20
Ladies Blowdry $20 from
Mens cut $15
Full head of Foils, Toner, Cut & Blowdry $110
Half Head of Foils, Toner, Cut & Blowdry $80
Tint cut & colour $60-80
Tint with scattered foils Cut & Blowdry $70-$110

Wedding Package Hair & Make up $135pp mobile servive provided
check out our webpage for our complete pricelist

prices subject to change without notice

business details:

p: 0491 826 374
E: lcs@quorvel.com.au
W: www.lumencrestsalon.com.au

I would like it to have maybe on the front as an initial eye catcher:

Full head of foils, Toner, Cut & Blowdry $110 every day

```html
<!DOCTYPE html>
<html lang="en">
<head>
<meta charset="utf-8">
<title>Lumencrest Salon – Flyer</title>
<link href="https://fonts.googleapis.com/css2?family=Marcellus&family=PT+Sans+Narrow&family=Patrick+Hand&family=Lora&display=swap" rel="stylesheet">
<style>
  :root {
    --pink: #d62a7a;
    --teal: #47b3c0;
    --ink: #161616;
    --cream: #fffdf0;
    --paper: #ffffff;
  }
  * { box-sizing: border-box; margin: 0; padding: 0; }
  html, body { width: 1200px; height: 772px; overflow: hidden; background: var(--paper); }
  .flyer {
    position: relative; width: 1200px; height: 772px; overflow: hidden;
    background: var(--paper); color: var(--ink);
    font-family: "PT Sans Narrow", "Arial Narrow", sans-serif;
  }
  .corner-tag { position: absolute; left: 0; top: 0; width: 267px; height: 267px; }
  .tagline {
    position: absolute; left: -40px; top: 72px; width: 300px;
    transform: rotate(-45deg); text-align: center; white-space: nowrap;
    font-family: "Lora", Georgia, serif; font-size: 20px; line-height: 23px;
    color: var(--pink);
  }
  .brand {
    position: absolute; left: 360px; top: 14px; width: 480px; text-align: center;
    font-family: "Marcellus", serif; color: var(--pink); font-weight: 400;
  }
  .brand-line1 { font-size: 80px; line-height: 78px; letter-spacing: 3px; }
  .brand-line2 { font-size: 62px; line-height: 66px; letter-spacing: 1px; }
  .hero-art {
    position: absolute; left: 450px; top: 175px; width: 240px; height: 400px;
    border-radius: 6px;
    background: linear-gradient(160deg, #f2f2f2 0%, #dcdcdc 55%, #c9c9c9 100%);
  }
  .offer {
    position: absolute; left: 936px; top: 40px; width: 182px; height: 182px;
    border-radius: 50%; background: var(--pink); color: #fff;
    display: flex; align-items: center; justify-content: center; text-align: center;
  }
  .offer p { transform: rotate(6deg); font-size: 21px; line-height: 25px; }
  .prices { position: absolute; left: 59px; top: 244px; width: 420px; font-size: 22px; }
  .prices h2 { font-weight: 400; font-size: 22px; text-decoration: underline; margin-bottom: 10px; }
  .price-list { list-style: none; }
  .price-list li { position: relative; line-height: 35.4px; }
  .price-list li::before {
    content: ""; position: absolute; left: -18px; top: 15px;
    width: 7px; height: 7px; border-radius: 50%; background: var(--pink);
  }
  .wedding { margin-top: 24px; line-height: 35px; }
  .more { margin-top: 22px; line-height: 35px; }
  .note { font-size: 19px; line-height: 30px; }
  .contact-card {
    position: absolute; left: 778px; top: 390px; width: 422px; height: 382px;
    background: var(--cream); box-shadow: -6px 4px 8px rgba(0,0,0,.45);
    font-family: "Patrick Hand", cursive; font-size: 26px; color: var(--ink);
  }
  .about { position: absolute; left: 40px; top: 28px; width: 350px; text-align: center; line-height: 36px; letter-spacing: .5px; }
  .contact-list { position: absolute; left: 30px; top: 167px; list-style: none; }
  .contact-list li { display: flex; align-items: center; height: 46px; font-size: 27px; letter-spacing: .5px; }
  .contact-list svg { width: 30px; height: 30px; margin-right: 16px; flex: none; }
</style>
</head>
<body>
<main class="flyer">
  <svg class="corner-tag" viewBox="0 0 267 267" aria-hidden="true">
    <polygon points="0,0 267,0 0,267" fill="var(--teal)"/>
  </svg>
  <p class="tagline">Look good,<br>feel great<br>without paying silly prices.</p>

  <h1 class="brand"><span class="brand-line1">LUMENCREST</span><br><span class="brand-line2">SALON</span></h1>

  <div class="hero-art" role="img" aria-label="Illustration of a leaping figure silhouette with flowing hair"></div>

  <div class="offer"><p>Full head of foils,<br>Toner, Cut &amp; Blowdry<br>$110 every day</p></div>

  <section class="prices">
    <h2>Price list:</h2>
    <ul class="price-list">
      <li>Ladies Cut $20</li>
      <li>Ladies Blowdry $20 from</li>
      <li>Mens cut $15</li>
      <li>Full head of Foils, Toner, Cut &amp; Blowdry $110</li>
      <li>Half Head of Foils, Toner, Cut &amp; Blowdry $80</li>
      <li>Tint cut &amp; colour $60-80</li>
      <li>Tint with scattered foils Cut &amp; Blowdry $70-$110</li>
    </ul>
    <p class="wedding">Wedding Package Hair &amp; Make up $135pp (mobile servive provided).</p>
    <p class="more">Check out our webpage for our complete pricelist.</p>
    <p class="note">Prices subject to change without notice.</p>
  </section>

  <aside class="contact-card">
    <p class="about">Private home salon based in „Corallin bay“. Mobile service provided for weddings only.</p>
    <ul class="contact-list">
      <li>
        <svg viewBox="0 0 24 24" aria-hidden="true"><path d="M6.6 2.5c.6-.3 1.3-.1 1.6.5l2 3.6c.3.6.2 1.2-.3 1.6L8.4 9.3c1 2.3 3.2 4.6 5.6 5.8l1.2-1.5c.4-.5 1.1-.6 1.6-.3l3.6 2c.6.3.8 1 .5 1.6l-1.2 2.4c-.4.8-1.3 1.3-2.2 1.1C10.2 19.3 4.8 13.8 3.6 6.5c-.2-.9.3-1.8 1.1-2.2z" fill="var(--ink)"/></svg>
        <span>&nbsp;0491 826 374</span>
      </li>
      <li>
        <svg viewBox="0 0 24 24" aria-hidden="true"><rect x="2.5" y="5" width="19" height="14" fill="none" stroke="var(--ink)" stroke-width="1.8"/><path d="M2.5 5l9.5 8 9.5-8M2.5 19l7-6.5M21.5 19l-7-6.5" fill="none" stroke="var(--ink)" stroke-width="1.6"/></svg>
        <span>lcs@quorvel.com.au</span>
      </li>
      <li>
        <svg viewBox="0 0 24 24" aria-hidden="true"><g fill="none" stroke="var(--ink)" stroke-width="1.5"><circle cx="12" cy="12" r="9.5"/><ellipse cx="12" cy="12" rx="4.5" ry="9.5"/><path d="M12 2.5v19M2.5 12h19M4 7h16M4 17h16"/></g></svg>
        <span>www.lumencrestsalon.com.au</span>
      </li>
    </ul>
  </aside>
</main>
</body>
</html>
```